Flyer für Personalreferentin
Zielgruppe
Freiberufliche Personalreferentin. Ich unterstütze Unternehmen (zeitweise) in den Personalabteilungen (Rekrutierung, Personalverwaltung, Mitarbeiterbetreuung). Zielgruppe sind Unternehmen, die moderne Personalarbeit abbilden möchten.
Aufgabenstellung
Der Flyer soll 2-seitig sein. Seite 1 - Werbetext und Seite 2 bzw. Rückseite mein Profil bzw. meinen Lebenslauf ansprechend dargestellt. Ich möchte ein modernes, minimalistisches Design.
Ziel wäre einen Flyer zu erhalten, den man an die Unternehmen senden kann um auf die Dienstleistung aufmerksam zu machen. Logo und Profilbild sollen verwendet werden, weitere Bilder gern mitvorschlagen.

```html
<!DOCTYPE html>
<html lang="de">
<head>
<meta charset="utf-8">
<title>Flyer HR Freelancer</title>
<link href="https://fonts.googleapis.com/css2?family=Poppins:wght@300;400;500;600;700;800&display=swap" rel="stylesheet">
<style>
:root{
  --red:#f05a4a;
  --pink:#fde2de;
  --dark:#555556;
  --stage:#737373;
  --ink:#3a3a3a;
  --white:#ffffff;
  --sky1:#cfe3f3;
  --sky2:#6f97bb;
}
*{box-sizing:border-box;margin:0;padding:0}
html,body{width:1200px;height:1117px;overflow:hidden;background:var(--stage);font-family:"Poppins",sans-serif;color:var(--ink)}
.page{position:absolute;top:170px;width:550px;height:777px;background:var(--white);overflow:hidden;box-shadow:4px 6px 10px rgba(0,0,0,.35)}
.page-front{left:39px}
.page-back{left:611px}
.shapes{position:absolute;left:0;top:0;width:550px;height:777px}

/* front */
.hero-photo{position:absolute;left:0;top:0;width:550px;height:240px;background:linear-gradient(160deg,var(--sky1) 0%,#a9c8e2 40%,var(--sky2) 100%);clip-path:polygon(33px 0,550px 0,550px 240px,6px 240px)}
.hero-band{position:absolute;left:6px;top:159px;width:544px;height:81px;background:rgba(85,85,86,.72)}
.hero-title{position:absolute;left:0;top:168px;width:550px;text-align:center;color:var(--white);font-weight:700;font-size:14.5px;line-height:18px}
.brand{position:absolute;text-align:center;color:var(--ink);white-space:nowrap}
.brand-name{font-weight:300;font-size:25px;line-height:28px;letter-spacing:.3px}
.brand-role{font-weight:400;font-size:11.5px;letter-spacing:.6px;margin-top:6px}
.front-brand{left:335px;top:72px;width:200px}
.intro{position:absolute;left:0;top:240px;width:550px;height:80px;background:var(--red);color:var(--white);text-align:center;font-size:10.2px;line-height:14px;padding-top:10px}
.benefits-title{position:absolute;left:0;top:334px;width:550px;text-align:center;color:var(--red);font-weight:700;font-size:10.2px}
.benefit-pill{position:absolute;width:205px;height:31px;background:var(--red);border-radius:0 16px 16px 0;box-shadow:4px 4px 0 var(--pink);color:var(--white);font-weight:700;font-size:11.5px;line-height:12.5px;display:flex;align-items:center;padding-left:40px}
.benefit-icon{position:absolute;width:42px;height:42px;border-radius:50%;background:var(--white);border:1.5px solid var(--red);margin-left:-10px}
.benefit-text{position:absolute;width:215px;font-size:9.2px;line-height:11px;color:var(--ink)}
.cta{position:absolute;left:330px;top:682px;width:200px;text-align:center;color:var(--white);font-weight:700;font-size:11.2px;line-height:14.5px}

/* back */
.back-brand{left:45px;top:72px;width:200px}
.portrait{position:absolute;left:38px;top:143px;width:212px;height:212px;border-radius:50%;background:radial-gradient(circle at 50% 40%,#d9c1a8 0%,#b89372 45%,#e6e6e8 75%)}
.person-name{position:absolute;left:0;top:374px;width:279px;text-align:center;color:var(--white);font-weight:700;font-size:35px;line-height:40px}
.name-rule{position:absolute;left:111px;top:420px;width:68px;height:1.5px;background:var(--white)}
.birth{position:absolute;left:37px;top:434px;color:var(--white);font-weight:700;font-size:10px}
.contact{position:absolute;left:0;width:261px;height:24px;border:1.3px solid var(--white);border-left:none;border-radius:0 12px 12px 0;color:var(--white);font-weight:700;font-size:10.4px;display:flex;align-items:center;padding-left:62px}
.contact svg{position:absolute;left:37px;top:6px;width:11px;height:11px}
.profile{position:absolute;left:37px;top:557px;width:215px;color:var(--white);font-size:9.2px;line-height:12.3px}
.lang{position:absolute;top:696px;width:100px;text-align:center;color:var(--white);font-size:9px;line-height:13px}
.lang b{font-weight:700;display:block}
.flag{width:28px;height:28px;border-radius:50%;margin:0 auto 4px}
.flag-en{background:radial-gradient(circle,#c8102e 0 18%,#ffffff 19% 30%,#1f3a8a 31%)}
.flag-es{background:linear-gradient(#c8102e 0 25%,#f6c400 25% 75%,#c8102e 75%)}
.section-title{position:absolute;left:252px;top:16px;width:298px;text-align:center;color:var(--white);font-weight:700;font-size:19.5px}
.job-head{position:absolute;left:287px;width:263px;height:28px;background:var(--pink);color:var(--red);font-weight:700;font-size:8.9px;line-height:11px;padding:3px 0 0 10px}
.job-list{position:absolute;left:299px;width:245px;list-style:none;font-size:7.4px;line-height:8.5px;color:var(--ink)}
.job-list li{position:relative;padding-left:15px;margin-bottom:3.2px}
.job-list li::before{content:"";position:absolute;left:0;top:2px;width:4.5px;height:4.5px;border-radius:50%;border:1.4px solid var(--red);background:var(--red);box-shadow:inset 0 0 0 1px var(--white)}
.job-list.loose li{margin-bottom:8.3px}
.job-list.mid li{margin-bottom:6.5px}
</style>
</head>
<body>

<section class="page page-front">
  <svg class="shapes" viewBox="0 0 550 777" aria-hidden="true">
    <rect x="0" y="0" width="40" height="240" fill="var(--red)"/>
    <polygon points="550,373 550,663 517,663" fill="var(--red)"/>
    <path d="M550 665 H352 C305 665 292 688 272 718 C252 748 238 768 205 770 H550 Z" fill="var(--dark)"/>
    <path d="M550 663 H350 C302 663 289 686 269 716 C249 746 235 766 203 768 H0" fill="none" stroke="var(--red)" stroke-width="3"/>
  </svg>
  <div class="hero-photo" role="img" aria-label="Foto: Glasfassade eines modernen Bürogebäudes vor blauem Himmel"></div>
  <div class="hero-band"></div>
  <h1 class="hero-title">Sie suchen einen erfahrenen Personalreferenten mit<br>einem modernen Verständnis von Personalarbeit<br>und Mitarbeiterführung?</h1>
  <div class="brand front-brand">
    <div class="brand-name">lena hartwig</div>
    <div class="brand-role">HR Freelancer</div>
  </div>
  <p class="intro">Ich biete Ihnen 10 Jahre Berufserfahrung, nachgewiesene Expertise in der<br>Personalentwicklung und Führung, sowie eine empathische, diskrete und zuverlässige<br>Arbeitsweise. Als freiberuflicher Personalreferent stehe ich Ihnen flexibel<br>und bedarfsgerecht zur Verfügung, um Ihr Unternehmen erfolgreich zu unterstützen.</p>
  <h2 class="benefits-title">Ein freiberuflicher Personalreferent bietet zudem eine Reihe von Vorteilen:</h2>

  <div class="benefit-pill" style="left:80px;top:364px">Flexibilität</div>
  <div class="benefit-icon" style="left:59px;top:359px"></div>
  <p class="benefit-text" style="left:49px;top:412px">Als Freiberufler können Personalreferenten flexibel auf die Anforderungen und Bedürfnisse eines Unternehmens reagieren. Sie können sowohl für kurzfristige Projekte als auch für langfristige Engagements engagiert werden, je nach Bedarf des Unternehmens.</p>

  <div class="benefit-pill" style="left:80px;top:498px">Fachkenntnisse und<br>Erfahrung</div>
  <div class="benefit-icon" style="left:59px;top:493px"></div>
  <p class="benefit-text" style="left:49px;top:544px">Freiberufliche Personalreferenten verfügen in der Regel über umfangreiche Fachkenntnisse und langjährige Erfahrung in verschiedenen Branchen. Sie bringen wertvolles Know-how und Best Practices mit, um effektive HR-Strategien und -Prozesse zu entwickeln und umzusetzen.</p>

  <div class="benefit-pill" style="left:80px;top:640px">Kostenersparnis</div>
  <div class="benefit-icon" style="left:59px;top:635px"></div>
  <p class="benefit-text" style="left:49px;top:685px">Die Beauftragung eines freiberuflichen Personalreferenten kann kostengünstiger sein als die Einstellung eines festangestellten Mitarbeiters. Unternehmen können die Kosten für Sozialleistungen, Lohnnebenkosten und Fortbildungsmaßnahmen einsparen.</p>

  <div class="benefit-pill" style="left:332px;top:364px">Spezialisierung</div>
  <div class="benefit-icon" style="left:311px;top:359px"></div>
  <p class="benefit-text" style="left:301px;top:412px">Freiberufliche Personalreferenten können auf bestimmte HR-Bereiche spezialisiert sein, wie z.B. Rekrutierung, Personalentwicklung oder Arbeitsrecht. Unternehmen können von dieser Spezialisierung profitieren und sich auf Expertenwissen verlassen, um spezifische HR-Herausforderungen anzugehen.</p>

  <div class="benefit-pill" style="left:332px;top:525px">Unabhängigkeit</div>
  <div class="benefit-icon" style="left:311px;top:520px"></div>
  <p class="benefit-text" style="left:301px;top:573px">Freiberufliche Personalreferenten arbeiten selbstständig und eigenverantwortlich. Sie bringen frische Perspektiven und neue Ideen in das Unternehmen ein, ohne von internen Strukturen oder Unternehmen-skulturen beeinflusst zu sein.</p>

  <p class="cta">Kontaktieren Sie mich jetzt,<br>um zu erfahren, wie ich<br>Ihre HR-Prozesse optimieren<br>und Ihr Team zum Erfolg<br>führen kann.</p>
</section>

<section class="page page-back">
  <svg class="shapes" viewBox="0 0 550 777" aria-hidden="true">
    <path d="M0 0 H550 V50 H302 C276 50 270 40 262 28 C252 12 245 6 225 6 H0 Z" fill="var(--red)"/>
    <rect x="0" y="249" width="279" height="413" fill="var(--red)"/>
    <rect x="0" y="662" width="279" height="115" fill="var(--dark)"/>
    <rect x="279" y="769" width="271" height="8" fill="var(--dark)"/>
    <circle cx="144" cy="249" r="121" fill="var(--white)"/>
  </svg>
  <div class="brand back-brand">
    <div class="brand-name">lena hartwig</div>
    <div class="brand-role">HR Freelancer</div>
  </div>
  <div class="portrait" role="img" aria-label="Profilfoto der Personalreferentin"></div>
  <h1 class="person-name">Lena Hartwig</h1>
  <div class="name-rule"></div>
  <p class="birth">Geburtsdatum/ -ort: 14.05.1988 in Pirna</p>

  <div class="contact" style="top:458px">
    <svg viewBox="0 0 12 12"><path d="M6 0.5a4 4 0 0 1 4 4c0 3-4 7-4 7s-4-4-4-7a4 4 0 0 1 4-4z" fill="var(--white)"/><circle cx="6" cy="4.5" r="1.5" fill="var(--red)"/></svg>
    Birkenallee 14 - 15366 Musterfeld
  </div>
  <div class="contact" style="top:491px">
    <svg viewBox="0 0 12 12"><circle cx="6" cy="6" r="6" fill="var(--white)"/><path d="M4 3 l1 2 -0.7 0.7 c0.5 1 1 1.5 2 2 l0.7-0.7 2 1 -0.5 1.3 c-2.5 0-5-2.5-5-5z" fill="var(--red)"/></svg>
    0176 12 34 56 78
  </div>
  <div class="contact" style="top:524px">
    <svg viewBox="0 0 12 12"><circle cx="6" cy="6" r="6" fill="var(--white)"/><rect x="3" y="4" width="6" height="4.2" fill="none" stroke="var(--red)" stroke-width="0.9"/><path d="M3 4 l3 2.4 3-2.4" fill="none" stroke="var(--red)" stroke-width="0.9"/></svg>
    mail@lenahartwig.de
  </div>
  <p class="profile">Für die Tätigkeit im Personalwesen bringe ich ein abgeschlossenes Studium im Personalbereich, aufgrund meiner Ausbildung zur Hotelfachfrau den notwendigen Dienstleistungsgedanken sowie umfassende praktische Erfahrungen in verschiedenen Bereichen der Personalarbeit.</p>

  <div class="lang" style="left:37px"><div class="flag flag-en" role="img" aria-label="Flagge Englisch"></div><b>Englisch</b>verhandlungssicher</div>
  <div class="lang" style="left:146px"><div class="flag flag-es" role="img" aria-label="Flagge Spanisch"></div><b>Spanisch</b>Grundkenntnisse</div>

  <h2 class="section-title">Berufliche Erfahrung</h2>

  <div class="job-head" style="top:58px">03.2018 - 12.2023 Norvatek Service<br>GmbH, BerlinHR Generalist</div>
  <ul class="job-list" style="top:91px">
    <li>Personalbetreuung und -verwaltung</li>
    <li>Vorbereitende Lohn- und Gehaltsabrechnung</li>
    <li>Durchführung des BEM-Verfahrens</li>
    <li>Rekrutierung</li>
  </ul>

  <div class="job-head" style="top:142px">09.2014 – 02.2018 Modena Textil Ltd. &amp; Co. KG,<br>Berlin und deutschlandweit</div>
  <ul class="job-list loose" style="top:176px">
    <li>HR Assistant Manager / Recruitment Manager</li>
    <li>Personalbetreuung und -verwaltung<br>Deutschlandweite Rekrutierung von Mitarbeitern<br>u.a. im Rahmen von Filialeröffnungen</li>
    <li>Durchführen von Bewerbungsinterviews<br>an Standorten bundesweit</li>
    <li>Begleitung des kompletten Einstellungsprozesses</li>
    <li>Unterstützung des Führungsteams</li>
    <li>Kontrolle der Gehaltsabrechnung und des<br>Berichtswesen</li>
    <li>Zusammenarbeit mit der Arbeitnehmervertretung</li>
  </ul>

  <div class="job-head" style="top:330px">08.2013 – 08.2014 Lindhaus Hotel Gruppe,<br>BerlinHR Coordinator</div>
  <ul class="job-list loose" style="top:361px">
    <li>Operative Personalarbeit von Recruiting inkl.</li>
    <li>Stellenausschreibungen, über Vertragsgestaltung,<br>zu Personalbetreuung<br>bis zur Abwicklung aller Formalitäten bei<br>Austritten</li>
    <li>Implementierung und Weiterentwicklung<br>bestehender HR- Prozesse</li>
    <li>Personalverwaltung einzelner Häuser europaweit,<br>inkl. vorbereitende Lohn- und Gehaltsabrechnung</li>
    <li>Präsentation des Unternehmens auf<br>Messen, Schulen etc.</li>
    <li>Mitarbeit an verschiedenen HR-Projekten wie z.B.<br>Einführung eines unternehmensweiten Sprachkurses</li>
  </ul>

  <div class="job-head" style="top:527px">09.2010 – 02.2011 Seeblick Hotel Berlin, Seeblick<br>Hotels &amp; Resorts, Berlin</div>
  <ul class="job-list mid" style="top:561px">
    <li>Praktikum in der Personalabteilung</li>
    <li>Vorbereitung und Abwicklung aller Formalitäten bei<br>der Einstellung neuer Mitarbeiter</li>
    <li>Pflegen der Online-Recruitingportale</li>
    <li>Gestaltung von Stellenanzeigen</li>
    <li>Berufsaus- und Weiterbildung</li>
  </ul>

  <div class="job-head" style="top:646px">10.2008 – 03.2012 Hochschule Spreeland Studium der<br>Betriebswirtschaftslehre</div>
  <ul class="job-list" style="top:679px">
    <li>Abschluss: Bachelor of Arts (B.A.)</li>
    <li>Schwerpunkt Personal und Organisation</li>
  </ul>

  <div class="job-head" style="top:705px;padding-top:8px">08.2006 - 07.2008 Elbufer Hotel Pirna</div>
  <ul class="job-list" style="top:738px">
    <li>Ausbildung zur Hotelfachfrau</li>
    <li>Fremdsprachenkenntnisse</li>
  </ul>
</section>

</body>
</html>
```